Design for a Service-Based Estimate

We want a design for an Estimate that will always be sent in PDF format. The estimate or proposal is a critical document that needs to plainly show the service items, item description but also needs to be attractive and professional looking. Our current estimate deliverable is attached but it looks really basic like a Word document

```html
<!DOCTYPE html>
<html lang="en">
<head>
<meta charset="utf-8">
<title>Estimate – Keystone Slab Co.</title>
<link href="https://fonts.googleapis.com/css2?family=Open+Sans:wght@400;600;700&display=swap" rel="stylesheet">
<style>
  :root{
    --bg:#ececee;
    --paper:#ffffff;
    --navy:#23223a;
    --red:#c94228;
    --ink:#2a2a30;
    --rule:#c9c9cf;
  }
  *{box-sizing:border-box;margin:0;padding:0}
  html,body{width:1200px;height:800px;overflow:hidden;background:var(--bg);font-family:"Open Sans",sans-serif;color:var(--ink)}
  .estimate{position:absolute;left:300px;top:12px;width:600px;height:776px;background:var(--paper);box-shadow:0 2px 10px rgba(0,0,0,.12);padding:34px 40px 0 40px}
  .header{display:flex;justify-content:space-between;align-items:flex-start}
  .brand{font-size:15px;font-weight:700;color:var(--navy);letter-spacing:.5px;margin-top:26px}
  .recipient{text-align:right;font-size:8px;line-height:1.45}
  .rule{border:0;border-top:1px solid var(--rule);margin:14px 0}
  .project{text-align:center;font-size:8.5px;line-height:1.5}
  .project-title{font-weight:700;font-size:9.5px}
  table.items{width:100%;border-collapse:collapse;font-size:8.5px;margin-top:6px}
  .items th{font-weight:700;text-align:left;padding:6px 4px;border-bottom:1px solid var(--rule);vertical-align:bottom}
  .items td{padding:7px 4px;vertical-align:top;line-height:1.45}
  .items .num{text-align:right;white-space:nowrap}
  .items .total{font-weight:700}
  .items tr.line td{border-bottom:1px solid var(--rule)}
  .items tr.sum td{font-weight:700;padding-top:8px}
  .terms{margin-top:26px}
  .terms h2{text-align:center;font-size:12px;font-weight:700;margin-bottom:12px}
  .terms ul{padding-left:16px;font-size:8.4px;line-height:1.55}
  .signatures{margin-top:34px;display:flex;gap:40px;padding-left:120px}
  .sig{width:150px;border-top:1px solid var(--ink);font-size:8.5px;padding-top:4px}
  .footer{position:absolute;left:0;bottom:0;width:600px;height:40px}
</style>
</head>
<body>
<main class="estimate">
  <header class="header">
    <div class="brand">KEYSTONE SLAB CO.</div>
    <address class="recipient" style="font-style:normal">
      To:<br>
      Dale Merriwether<br>
      48 Harbor Lane SE Fernport 30219<br>
      dmerriwether@mailbox.example
    </address>
  </header>
  <hr class="rule">
  <section class="project">
    <div class="project-title">Dale Merriwether New Concrete Pad</div>
    <div>48 Harbor Lane SE Fernport 30219</div>
    <div>Bid#: 20-0182</div>
  </section>
  <hr class="rule">
  <table class="items">
    <thead>
      <tr><th style="width:58%">Item</th><th class="num">Quantity</th><th>U/M</th><th class="num">Unit $</th><th class="num">Total $</th></tr>
    </thead>
    <tbody>
      <tr><td>Form, Pour &amp; Finish New Concrete Slab (24' x 24' x 4"). Includes: 3000psi Concrete Mix, Footer (12" x 8") with One (#5) Continuous Rebar, Wire Mesh Reinforcement and Saw-Cut Expansion Joints</td><td class="num">576</td><td>SF</td><td class="num">$8.65</td><td class="num total">$4,982.40</td></tr>
      <tr class="line"><td>OPTIONAL: Add (2' x 24' x 4") Small Ramp Area</td><td class="num">48</td><td>SF</td><td class="num">$8.65</td><td class="num total">$415.20</td></tr>
      <tr class="sum"><td></td><td></td><td colspan="2" class="num">Total Price</td><td class="num">$5,397.60</td></tr>
    </tbody>
  </table>
  <section class="terms">
    <h2>Terms and Conditions</h2>
    <ul>
      <li>Prices as quoted in this estimate are valid for (60) days only.</li>
      <li>Payment in full, less any previously paid amounts, is due to the Contractor upon completion of the proposed scope of work.</li>
      <li>All change order requests must be communicated in writing to the Contractor by the Client or their authorized representative.</li>
      <li>All measurements listed in this estimate are approximate and may vary slightly due to actual field conditions.</li>
      <li>It is agreed by the Contractor and the Client that complications and costs arising from unforeseen conditions and handling of unsuitable materials are not included in this estimate.</li>
      <li>Unless specifically listed in this estimate, the following items and their costs are not included: Maintenance of Traffic, Concrete Material Pumping, Testing, Excavation, Grading and Fill Material, Permits and Fees, Surveying and As-builts, Irrigation Repair, Landscaping and Root Mitigation, De-watering, Private Locates and Accessibility.</li>
      <li>Private utility locating services using radio detection devices and, when necessary, ground penetrating radar are offered by Keystone Slab Co. to assist in finding private utilities that may not have been located by the public one call system. Keystone Slab Co. will not be responsible for private utilities that have not been located nor for the failure of the above equipment to accurately detect existing utilities since the equipment is fallible and existing site conditions may preclude the ability of the equipment to detect an identifiable signal.</li>
    </ul>
  </section>
  <section class="signatures">
    <div class="sig">Client Signature</div>
    <div class="sig">Date</div>
  </section>
  <svg class="footer" viewBox="0 0 600 40" aria-hidden="true">
    <rect x="0" y="0" width="600" height="40" fill="var(--navy)"/>
    <polygon points="0,12 262,12 282,34 0,34" fill="#ffffff"/>
    <polygon points="0,15 259,15 276,34 0,34" fill="var(--red)"/>
    <rect x="0" y="34" width="600" height="6" fill="var(--navy)"/>
  </svg>
</main>
</body>
</html>
```